Branded Resources for ORBALQa--Word, PPT, Newsletter Templates

Hi,
I hope you are well. I am hoping to get some pricing on branding a Word and PPT template and a Newsletter template. I've uploaded the original files for quick reference.

I was hoping for a full-color version and a black/grayscale version of the word and PPT template. Full color for the newsletter.

Thanks in advance for your quote and expected timeline for this project.

Thanks,
Velisse
Updates

Thank you for your submission and patience. I had a family emergency, and just getting back online. I will review the submissions. Thank you. Velisse

Industry/Entity Type

management consulting. Here's my website: https://orbalqa.example/

Requirements
Must have
• The Word, PPT and Newsletter templates should reflect the logo assets listed below. Open to complementary colors that complement red/orange/golds
Nice to have
• Vibrancy, diversity, community

```html
<!DOCTYPE html>
<html lang="en">
<head>
<meta charset="utf-8">
<title>ORBALQa Letterhead</title>
<link rel="stylesheet" href="https://fonts.googleapis.com/css2?family=Montserrat:wght@400;600&family=Roboto+Condensed:wght@400&display=swap">
<style>
:root{
  --stage:#666666;
  --paper:#ffffff;
  --brand:#7a2a24;
  --ink:#575757;
  --heading:#333333;
  --mark:#1a1a1a;
  --tint:#f6f3ec;
}
*{box-sizing:border-box;margin:0;padding:0}
html,body{width:1200px;height:960px;overflow:hidden;background:var(--stage)}
.sheet{position:absolute;top:145px;width:518px;height:670px;background:var(--paper);overflow:hidden;font-family:"Montserrat",sans-serif;color:var(--ink)}
.sheet--cover{left:63px}
.sheet--follow{left:619px}
.backdrop-disc{position:absolute;left:15px;top:114px;width:490px;height:490px;border-radius:50%;background:var(--tint)}
.brand{position:absolute;left:47px;top:20px;display:flex;flex-direction:column;align-items:center;gap:6px;width:80px}
.brand-dot{width:72px;height:72px;border-radius:50%;background:var(--mark)}
.brand-name{font-family:"Montserrat",sans-serif;font-weight:600;font-size:12px;color:var(--mark);letter-spacing:.5px}
.title-frame{position:absolute;left:224px;top:124px;width:294px;height:43px;border:3px solid var(--brand);border-left:none}
.title-frame::before,.title-frame::after{content:"";position:absolute;left:0;width:3px;height:7px;background:var(--brand)}
.title-frame::before{top:0}
.title-frame::after{bottom:0}
.title{position:absolute;left:205px;top:136px;font-weight:600;font-size:14.4px;color:var(--heading);white-space:nowrap}
.running-title{position:absolute;right:48px;top:64px;font-weight:600;font-size:8.6px;color:var(--brand);white-space:nowrap}
.copy{position:absolute;left:47px;width:424px;font-size:9.45px;line-height:14.15px;z-index:1}
.copy p+p{margin-top:11.5px}
.copy--intro{top:188px}
.columns{position:absolute;left:47px;width:424px;display:flex;gap:24px;font-size:9.45px;line-height:14.15px;z-index:1}
.columns--cover{top:341px}
.columns--follow{top:140px}
.column{width:200px}
.column p+p{margin-top:11.5px}
.contact-bar{position:absolute;left:0;top:641px;width:100%;height:14px;font-family:"Roboto Condensed",sans-serif;font-size:6.9px;color:#222;z-index:1}
.contact{position:absolute;top:0;display:flex;align-items:center;gap:5px;white-space:nowrap}
.contact svg{width:9px;height:9px}
.contact--phone{left:47px}
.contact--mail{left:129px}
.contact--web{left:252px}
.contact--place{left:367px}
.base-band{position:absolute;left:0;bottom:0;width:100%;height:13px;background:var(--brand)}
</style>
</head>
<body>

<section class="sheet sheet--cover">
  <div class="backdrop-disc"></div>
  <div class="brand"><span class="brand-dot"></span><span class="brand-name">ORBALQa</span></div>
  <div class="title-frame"></div>
  <h1 class="title">TITTLE LOREMIPSUM DOLORSITAMET</h1>
  <div class="copy copy--intro">
    <p>Lorem ipsum dolor sit amet, consectetur adipiscing elit. Duis auctor sem vel metus interdum porta. Duis consequat bibendum felis eget cursus. Nulla eget purus vehicula ipsum finibus egestas. Nullam ligula ipsum, mollis sed gravida vitae, maximus eu dolor. Morbi luctus sem a congue consectetur.</p>
    <p>Orci varius natoque penatibus et magnis dis parturient montes, nascetur ridiculus mus. Vestibulum congue eros auctor, ullamcorper libero blandit, tempor tellus. Proin vitae tellus et nunc fringilla lacinia. Sed augue erat, facilisis laoreet velit a, convallis mattis nunc. Nunc sagittis ligula vitae sollicitudin sollicitudin. Orci varius natoque penatibus et magnis dis parturient montes, nascetur ridiculus mus. Vestibulum congue eros auctor, ullamcorper.</p>
  </div>
  <div class="columns columns--cover">
    <div class="column">
      <p>Lorem ipsum dolor sit amet, consectetur adipiscing elit. Duis auctor sem vel metus interdum porta. Duis consequat bibendum felis eget cursus. Nulla eget purus vehicula ipsum finibus egestas. Nullam ligula ipsum, mollis sed gravida vitae, maximus eu dolor. Morbi luctus sem a congue consectetur.</p>
      <p>Orci varius natoque penatibus et magnis dis parturient montes, nascetur ridiculus mus. Vestibulum congue eros auctor, ullamcorper libero blandit, tempor tellus. Proin vitae tellus et nunc fringilla lacinia. Sed augue erat, facilisis laoreet velit a, convallis mattis nunc. Nunc sagittis ligula vitae sollicitudin sollicitudin. Orci varius natoque penatibus et magnis dis parturient montes, nascetur ridiculus mus.</p>
    </div>
    <div class="column">
      <p>Vestibulum congue eros auctor, ullamcorper libero blandit, tempor tellus. Proin vitae tellus et nunc fringilla lacinia. Sed augue erat, facilisis laoreet velit a, convallis mattis nunc. Nunc sagittis ligula vitae sollicitudin sollicitudin.</p>
      <p>Nulla facilisi. Nulla quis odio vitae purus aliquam fermentum ut nec diam. Fusce sed velit ultrices, aliquam augue ut, sollicitudin orci. Orci varius natoque penatibus et magnis dis parturient montes, nascetur ridiculus mus. Vestibulum congue eros auctor, ullamcorper libero blandit, tempor tellus. Proin vitae tellus et nunc fringilla lacinia. Sed augue erat, facilisis laoreet velit a, convallis mattis nunc. Nunc sagittis ligula vitae sollicitudin sollicitudin.</p>
    </div>
  </div>
  <footer class="contact-bar">
    <span class="contact contact--phone"><svg viewBox="0 0 10 10"><circle cx="5" cy="5" r="5" fill="#7a2a24"/><rect x="3.3" y="2.2" width="3.4" height="5.6" rx=".6" fill="none" stroke="#fff" stroke-width=".9"/></svg>0123 456 790</span>
    <span class="contact contact--mail"><svg viewBox="0 0 10 10"><circle cx="5" cy="5" r="5" fill="#7a2a24"/><rect x="2.6" y="3.3" width="4.8" height="3.4" fill="none" stroke="#fff" stroke-width=".8"/><path d="M2.6 3.3 5 5.2 7.4 3.3" fill="none" stroke="#fff" stroke-width=".8"/></svg>info@yourwebnamae.com</span>
    <span class="contact contact--web"><svg viewBox="0 0 10 10"><circle cx="5" cy="5" r="5" fill="#7a2a24"/><circle cx="5" cy="5" r="2.8" fill="none" stroke="#fff" stroke-width=".7"/><path d="M2.2 5h5.6M5 2.2v5.6" stroke="#fff" stroke-width=".6"/></svg>www.yourwebnamae.com</span>
    <span class="contact contact--place"><svg viewBox="0 0 10 10"><path d="M5 .5a3.8 3.8 0 0 1 3.8 3.8C8.8 7 5 9.7 5 9.7S1.2 7 1.2 4.3A3.8 3.8 0 0 1 5 .5z" fill="#7a2a24"/><circle cx="5" cy="4.3" r="1.4" fill="#fff"/></svg>1235456, your location.23923923</span>
  </footer>
  <div class="base-band"></div>
</section>

<section class="sheet sheet--follow">
  <div class="backdrop-disc"></div>
  <div class="brand"><span class="brand-dot"></span><span class="brand-name">ORBALQa</span></div>
  <h2 class="running-title">TITTLE LOREMIPSUM DOLORSITAMET</h2>
  <div class="columns columns--follow">
    <div class="column">
      <p>Lorem ipsum dolor sit amet, consectetur adipiscing elit. Duis auctor sem vel metus interdum porta. Duis consequat bibendum felis eget cursus. Nulla eget purus vehicula ipsum finibus egestas. Nullam ligula ipsum, mollis sed gravida vitae, maximus eu dolor. Morbi luctus sem a congue consectetur.</p>
      <p>Orci varius natoque penatibus et magnis dis parturient montes, nascetur ridiculus mus. Vestibulum congue eros auctor, ullamcorper libero blandit, tempor tellus. Proin vitae tellus et nunc fringilla lacinia. Sed augue erat, facilisis laoreet velit a, convallis mattis nunc. Nunc sagittis ligula vitae sollicitudin sollicitudin. Orci varius natoque penatibus et magnis dis parturient montes, nascetur ridiculus mus. Vestibulum congue eros auctor, ullamcorper.</p>
      <p>Lorem ipsum dolor sit amet, consectetur adipiscing elit. Duis auctor sem vel metus interdum porta. Duis consequat bibendum felis eget cursus. Nulla eget purus vehicula ipsum finibus egestas. Nullam ligula ipsum, mollis sed gravida vitae, maximus eu dolor. Morbi luctus sem a congue consectetur.Orci varius natoque penatibus et magnis dis parturient montes, nascetur ridiculus mus. Vestibulum congue eros auctor,</p>
    </div>
    <div class="column">
      <p>ullamcorper libero blandit, tempor tellus. Proin vitae tellus et nunc fringilla lacinia. Sed augue erat, facilisis laoreet velit a, convallis mattis nunc. Nunc sagittis ligula vitae sollicitudin sollicitudin. Orci varius natoque penatibus et magnis dis parturient montes, nascetur ridiculus mus.</p>
      <p>Vestibulum congue eros auctor, ullamcorper libero blandit, tempor tellus. Proin vitae tellus et nunc fringilla lacinia. Sed augue erat, facilisis laoreet velit a, convallis mattis nunc. Nunc sagittis ligula vitae sollicitudin sollicitudin.</p>
      <p>Nulla facilisi. Nulla quis odio vitae purus aliquam fermentum ut nec diam. Fusce sed velit ultrices, aliquam augue ut, sollicitudin orci. Orci varius natoque penatibus et magnis dis parturient montes, nascetur ridiculus mus. Vestibulum congue eros auctor, ullamcorper libero blandit, tempor tellus. Proin vitae tellus et nunc fringilla lacinia. Sed augue erat, facilisis laoreet velit a, convallis mattis nunc. Nunc sagittis ligula vitae sollicitudin sollicitudin. atibus et magnis dis parturient montes, nascetur ridiculus mus. Vestibuluatibus et magnis dis parturient montes, nascetur ridiculus mus. Vestibuluatibus et magnis dis parturient montes, nascetur ridiculus mus. Vestibulu.</p>
    </div>
  </div>
  <footer class="contact-bar">
    <span class="contact contact--phone"><svg viewBox="0 0 10 10"><circle cx="5" cy="5" r="5" fill="#7a2a24"/><rect x="3.3" y="2.2" width="3.4" height="5.6" rx=".6" fill="none" stroke="#fff" stroke-width=".9"/></svg>0123 456 790</span>
    <span class="contact contact--mail"><svg viewBox="0 0 10 10"><circle cx="5" cy="5" r="5" fill="#7a2a24"/><rect x="2.6" y="3.3" width="4.8" height="3.4" fill="none" stroke="#fff" stroke-width=".8"/><path d="M2.6 3.3 5 5.2 7.4 3.3" fill="none" stroke="#fff" stroke-width=".8"/></svg>info@yourwebnamae.com</span>
    <span class="contact contact--web"><svg viewBox="0 0 10 10"><circle cx="5" cy="5" r="5" fill="#7a2a24"/><circle cx="5" cy="5" r="2.8" fill="none" stroke="#fff" stroke-width=".7"/><path d="M2.2 5h5.6M5 2.2v5.6" stroke="#fff" stroke-width=".6"/></svg>www.yourwebnamae.com</span>
    <span class="contact contact--place"><svg viewBox="0 0 10 10"><path d="M5 .5a3.8 3.8 0 0 1 3.8 3.8C8.8 7 5 9.7 5 9.7S1.2 7 1.2 4.3A3.8 3.8 0 0 1 5 .5z" fill="#7a2a24"/><circle cx="5" cy="4.3" r="1.4" fill="#fff"/></svg>1235456, your location.23923923</span>
  </footer>
  <div class="base-band"></div>
</section>

</body>
</html>
```